International Wine Label 202001

Need a wine label designed for several new wines from California being exported to Asia. This label should be focused around an animal theme of the flowing: Tiger, Lion, Horse or Eagle. The label should be adaptable to a product line of wines. For example the label could be used for a Cabernet wine, Merlot, Chardonnay or Pinot. A slight modification to the label design should be incorporated to allow for the different varietals. Front label design only. Can utilize photo image in design.
The label would be around 5.75" x 3.50".

Target Market(s)

25-35 year old wine buyers in the global market

Industry/Entity Type

Retail

Font styles to use
Sans Serif

Requirements
Must have
• Wine name based on design (designer suggest name)
Wine varietals
Vintage date
Additional wording area
Nice to have
• Rectangular label preferred Front label only.

```html
<!DOCTYPE html>
<html lang="en">
<head>
<meta charset="utf-8">
<title>Proud Dawn — Varietal Label Series</title>
<link rel="stylesheet" href="https://fonts.googleapis.com/css2?family=Caveat+Brush&family=Permanent+Marker&family=Kaushan+Script&family=Allura&family=Great+Vibes&family=Old+Standard+TT:wght@400;700&display=swap">
<style>
  :root {
    --page-bg: #f1f1f4;
    --label-light: #eeeeef;
    --label-mid: #d3d3d6;
    --label-edge: #c4c4c8;
    --ink: #141414;
    --merlot: #3e4a6e;
    --pinot: #6b1de6;
    --chardonnay: #d6b21c;
    --cabernet: #a4213f;
    --smudge: rgba(150,150,155,0.45);
  }
  * { box-sizing: border-box; margin: 0; padding: 0; }
  html, body {
    width: 1200px; height: 1100px; overflow: hidden;
    background: var(--page-bg);
  }
  .label-series {
    position: absolute; inset: 0;
    display: flex; justify-content: center; align-items: center;
    gap: 22px;
  }
  .wine-label {
    width: 268px; height: 420px;
    position: relative;
    background:
      radial-gradient(circle at 80% 20%, rgba(255,255,255,0.55) 0 18px, transparent 40px),
      radial-gradient(circle at 20% 78%, rgba(255,255,255,0.45) 0 20px, transparent 44px),
      radial-gradient(ellipse at 50% 45%, var(--label-light) 0%, var(--label-mid) 75%, var(--label-edge) 100%);
    box-shadow: 0 2px 8px rgba(0,0,0,0.12);
    display: flex; flex-direction: column; align-items: center;
    padding-top: 16px;
  }
  .brand-name {
    font-family: "Caveat Brush", "Permanent Marker", cursive;
    font-weight: 400;
    color: var(--ink);
    font-size: 50px; line-height: 0.82;
    text-align: center; letter-spacing: 0;
    text-transform: uppercase;
  }
  .brand-name span { display: block; }
  .brand-name .line-two { margin-left: -12px; }
  .emblem-area {
    position: relative;
    width: 200px; height: 210px;
    margin-top: 24px;
  }
  .emblem-smudge {
    position: absolute; left: 8px; top: 55px;
    width: 184px; height: 110px;
    background: radial-gradient(ellipse at center, var(--smudge) 0%, rgba(150,150,155,0.2) 60%, transparent 75%);
    border-radius: 40% 55% 45% 50%;
  }
  .lion-illustration {
    position: absolute; left: 30px; top: 0;
    width: 140px; height: 205px;
    border-radius: 48% 48% 46% 46% / 40% 40% 60% 60%;
    background: radial-gradient(ellipse at 50% 45%, rgba(255,255,255,0.7) 0%, var(--tone) 95%);
    opacity: 0.55;
  }
  .varietal {
    font-weight: 400;
    color: var(--tone);
    line-height: 1;
    white-space: nowrap;
    border-bottom: 1px solid var(--tone);
    padding: 0 4px 1px;
  }
  .merlot { --tone: var(--merlot); }
  .pinot { --tone: var(--pinot); }
  .chardonnay { --tone: var(--chardonnay); }
  .cabernet { --tone: var(--cabernet); }
  .merlot .varietal { font-family: "Allura", cursive; font-size: 54px; margin-top: 8px; }
  .pinot .varietal { font-family: "Kaushan Script", cursive; font-size: 32px; margin-top: 18px; }
  .chardonnay .varietal { font-family: "Kaushan Script", cursive; font-size: 28px; margin-top: 20px; }
  .cabernet .varietal { font-family: "Great Vibes", cursive; font-size: 26px; margin-top: 24px; }
  .vintage {
    font-family: "Old Standard TT", serif;
    color: var(--ink);
    font-size: 12.5px; line-height: 1.05;
    text-align: center; letter-spacing: 0.5px;
    margin-top: 3px;
  }
</style>
</head>
<body>
  <main class="label-series">
    <article class="wine-label merlot">
      <h1 class="brand-name"><span>Proud</span><span class="line-two">Dawn</span></h1>
      <div class="emblem-area">
        <div class="emblem-smudge"></div>
        <div class="lion-illustration" role="img" aria-label="Line-art lion head illustration in navy over a grey brush smudge"></div>
      </div>
      <h2 class="varietal">Merlot</h2>
      <p class="vintage">VINTAGE DATE<br>2020</p>
    </article>
    <article class="wine-label pinot">
      <h1 class="brand-name"><span>Proud</span><span class="line-two">Dawn</span></h1>
      <div class="emblem-area">
        <div class="emblem-smudge"></div>
        <div class="lion-illustration" role="img" aria-label="Line-art lion head illustration in violet over a grey brush smudge"></div>
      </div>
      <h2 class="varietal">Pinot Noir</h2>
      <p class="vintage">VINTAGE DATE<br>2020</p>
    </article>
    <article class="wine-label chardonnay">
      <h1 class="brand-name"><span>Proud</span><span class="line-two">Dawn</span></h1>
      <div class="emblem-area">
        <div class="emblem-smudge"></div>
        <div class="lion-illustration" role="img" aria-label="Line-art lion head illustration in gold over a grey brush smudge"></div>
      </div>
      <h2 class="varietal">Chardonnay</h2>
      <p class="vintage">VINTAGE DATE<br>2020</p>
    </article>
    <article class="wine-label cabernet">
      <h1 class="brand-name"><span>Proud</span><span class="line-two">Dawn</span></h1>
      <div class="emblem-area">
        <div class="emblem-smudge"></div>
        <div class="lion-illustration" role="img" aria-label="Line-art lion head illustration in crimson over a grey brush smudge"></div>
      </div>
      <h2 class="varietal">Cabernet Sauvignon</h2>
      <p class="vintage">VINTAGE DATE<br>2020</p>
    </article>
  </main>
</body>
</html>
```